Modern, Sleek & Vibrant design required for electrical contracting work.

I require a flyer design for BRANDEL VOLT SERVICES, which operates as an electrical contractor. We do electrical installations such as LED lighting, maintenance, repairs, communications and various other work related for residential and commercial customers. I would like the same colours applied from my logo to the flyer (Electric Blue, White, Grey/Silver). A6 or DL sizes with single side.

Target Market(s)

Residential and Commercial customers.

Industry/Entity Type

Communications

Font styles to use
Serif
Sans Serif

Requirements
Must have
• My logo and colours (Electric Blue, White, Silver/Grey)
Nice to have
• Shapes separating different parts of the flyer, such as the same electric bolt from my logo. Straight or angled shapes.
Should not have
• Childish pictures such as light bulbs. Curved shapes.

```html
<!DOCTYPE html>
<html lang="en">
<head>
<meta charset="utf-8">
<title>Brandel Volt Services – Flyer</title>
<link href="https://fonts.googleapis.com/css2?family=Fira+Sans:wght@300;400;600&display=swap" rel="stylesheet">
<style>
  :root {
    --electric-blue: #3a53a4;
    --silver: #a8a8aa;
    --white: #ffffff;
    --ink-white: #f4f6fb;
  }
  html, body {
    margin: 0;
    padding: 0;
    width: 851px;
    height: 1200px;
    overflow: hidden;
    background: var(--white);
  }
  .flyer {
    position: relative;
    width: 851px;
    height: 1200px;
    overflow: hidden;
    background: var(--electric-blue);
    font-family: "Fira Sans", Arial, sans-serif;
    color: var(--ink-white);
  }
  .bolt-panel {
    position: absolute;
    inset: 0;
  }
  .company-title {
    position: absolute;
    left: 38px;
    top: 72px;
    margin: 0;
    font-size: 36px;
    font-weight: 600;
    letter-spacing: 0.3px;
    color: var(--white);
  }
  .title-rule {
    position: absolute;
    left: 38px;
    top: 122px;
    width: 508px;
    height: 1.5px;
    background: var(--white);
  }
  .service-list {
    position: absolute;
    left: 34px;
    top: 175px;
    margin: 0;
    padding: 0;
    list-style: none;
  }
  .service-list li {
    display: flex;
    align-items: center;
    height: 55px;
    font-size: 41px;
    font-weight: 300;
    color: var(--white);
  }
  .service-icon {
    width: 34px;
    height: 34px;
    margin-right: 16px;
    flex: none;
  }
  .quote-badge {
    position: absolute;
    left: 612px;
    top: 88px;
    width: 215px;
    height: 215px;
  }
  .quote-text {
    position: absolute;
    left: 620px;
    top: 117px;
    width: 190px;
    text-align: center;
    color: var(--electric-blue);
    font-weight: 300;
    line-height: 1;
  }
  .quote-text .small { display: block; font-size: 34px; }
  .quote-text .large { display: block; font-size: 46px; margin: 2px 0; }
  .director {
    position: absolute;
    left: 38px;
    top: 742px;
  }
  .director-role {
    margin: 0;
    font-size: 25px;
    font-weight: 600;
    color: var(--white);
  }
  .director-rule {
    width: 275px;
    height: 1.5px;
    background: var(--white);
    margin: 8px 0 6px;
  }
  .director-name {
    margin: 0;
    font-size: 29px;
    font-weight: 300;
    letter-spacing: 0.4px;
  }
  .director-contact {
    margin: 22px 0 0;
    font-size: 20px;
    font-weight: 300;
    line-height: 1.45;
  }
  .brand-mark {
    position: absolute;
    left: 296px;
    top: 1028px;
    display: flex;
    align-items: center;
  }
  .brand-dot {
    width: 104px;
    height: 104px;
    border-radius: 50%;
    background: var(--electric-blue);
    margin-right: 22px;
    flex: none;
  }
  .brand-name {
    margin: 0;
    font-size: 46px;
    font-weight: 600;
    line-height: 1.05;
    color: var(--electric-blue);
    letter-spacing: 1px;
  }
</style>
</head>
<body>
<main class="flyer">
  <svg class="bolt-panel" width="851" height="1200" viewBox="0 0 851 1200" aria-hidden="true">
    <defs>
      <linearGradient id="silverFade" x1="0" y1="0" x2="0.25" y2="1">
        <stop offset="0" stop-color="#a5a5a7"/>
        <stop offset="0.45" stop-color="#d9d9da"/>
        <stop offset="0.8" stop-color="#ffffff"/>
      </linearGradient>
    </defs>
    <polygon fill="url(#silverFade)"
      points="728,0 851,0 851,1200 130,1200 602,702 374,696 697,330 490,300"/>
  </svg>

  <h1 class="company-title">BRANDEL VOLT SERVICES</h1>
  <div class="title-rule"></div>

  <ul class="service-list">
    <li><svg class="service-icon" viewBox="0 0 34 34" aria-hidden="true"><circle cx="17" cy="17" r="14" fill="none" stroke="#fff" stroke-width="2.4"/><polygon points="20,6 11,19 16,19 13,28 23,14 18,14" fill="#fff"/></svg>LED Lighting</li>
    <li><svg class="service-icon" viewBox="0 0 34 34" aria-hidden="true"><circle cx="17" cy="17" r="14" fill="none" stroke="#fff" stroke-width="2.4"/><polygon points="20,6 11,19 16,19 13,28 23,14 18,14" fill="#fff"/></svg>Installations</li>
    <li><svg class="service-icon" viewBox="0 0 34 34" aria-hidden="true"><circle cx="17" cy="17" r="14" fill="none" stroke="#fff" stroke-width="2.4"/><polygon points="20,6 11,19 16,19 13,28 23,14 18,14" fill="#fff"/></svg>Maintenance</li>
    <li><svg class="service-icon" viewBox="0 0 34 34" aria-hidden="true"><circle cx="17" cy="17" r="14" fill="none" stroke="#fff" stroke-width="2.4"/><polygon points="20,6 11,19 16,19 13,28 23,14 18,14" fill="#fff"/></svg>Repairs</li>
    <li><svg class="service-icon" viewBox="0 0 34 34" aria-hidden="true"><circle cx="17" cy="17" r="14" fill="none" stroke="#fff" stroke-width="2.4"/><polygon points="20,6 11,19 16,19 13,28 23,14 18,14" fill="#fff"/></svg>Communications</li>
    <li><svg class="service-icon" viewBox="0 0 34 34" aria-hidden="true"><circle cx="17" cy="17" r="14" fill="none" stroke="#fff" stroke-width="2.4"/><polygon points="20,6 11,19 16,19 13,28 23,14 18,14" fill="#fff"/></svg>Emergency Call-Outs</li>
  </ul>

  <svg class="quote-badge" viewBox="0 0 215 215" aria-hidden="true">
    <circle cx="104" cy="104" r="86" fill="none" stroke="var(--electric-blue)" stroke-width="5"/>
    <path d="M 40 175 A 100 100 0 0 0 200 60" fill="none" stroke="var(--electric-blue)" stroke-width="3.5"/>
  </svg>
  <p class="quote-text">
    <span class="small">GET A</span>
    <span class="large">FREE</span>
    <span class="small">QUOTE</span>
  </p>

  <section class="director">
    <h2 class="director-role">DIRECTOR</h2>
    <div class="director-rule"></div>
    <p class="director-name">Daniel Brandel</p>
    <p class="director-contact">EC Number – EC20463<br>daniel@brandelvolt.com</p>
  </section>

  <div class="brand-mark">
    <div class="brand-dot"></div>
    <p class="brand-name">BRANDEL VOLT<br>SERVICES</p>
  </div>
</main>
</body>
</html>
```